Create a channel art for human resources youtube channel

We a are human resource company that want to develop a community on youtube. Our channel is call "TKV Corner" and we will produce videos related to human resources topics like: Strategy, Job Description, selection of workers, workers development, Occupational health, Training, etc.

We need a channel art for our youtube channel that communicate to our viewers what is about the channel.

Attach you can see the logo and icon of the channel, also you can see it here: https://www.vidzora-example.net/channel/QXpLmWt7bRc3dYhFvKaNsEeZ

Target Market(s)

The people who is going to see the art - banner for youtube are persons that work on human resources field

Industry/Entity Type

Business

Font styles to use
Sans Serif

Requirements
Must have
• Must to communicate that our channel is about how to do a better and faster human resources to help business improve there productivity , also workers performances and quality work life. Here are some key words to help you inspire:
• Human Resources
• Performance
• Better
• Faster
• Easier
• Business
• Improve
• Health

```html
<!DOCTYPE html>
<html lang="en">
<head>
<meta charset="utf-8">
<title>TKV Corner – Channel Art</title>
<link rel="stylesheet" href="https://fonts.googleapis.com/css2?family=Mulish:wght@400;500;800&display=swap">
<style>
  :root{
    --page-top:#ececec;
    --page-mid:#ffffff;
    --page-bottom:#f0f0f0;
    --red:#e0292c;
    --red-dark:#c81f24;
    --yellow:#f7c518;
    --blue:#22a6dc;
    --ink:#222222;
    --grey:#6b6b6b;
    --headline-yellow:#ffd21a;
    --white:#ffffff;
  }
  *{box-sizing:border-box;margin:0;padding:0}
  html,body{width:1200px;height:1200px;overflow:hidden}
  body{
    background:linear-gradient(180deg,var(--page-top) 0%,var(--page-mid) 30%,var(--page-mid) 70%,var(--page-bottom) 100%);
    font-family:"Mulish",sans-serif;
    position:relative;
  }
  .banner{
    position:absolute;left:101px;top:530px;width:1000px;height:141px;
    background:linear-gradient(180deg,#f2f2f2 0%,#ffffff 45%,#ededed 100%);
    box-shadow:0 2px 4px rgba(0,0,0,.18);
    overflow:hidden;
  }
  .shapes{position:absolute;inset:0;width:1000px;height:141px}
  .brand{
    position:absolute;left:45px;top:39px;height:74px;display:flex;align-items:center;gap:8px;
  }
  .brand-mark{
    width:73px;height:73px;border-radius:50%;
    border:2px solid #9a9a9a;background:var(--white);flex:none;
  }
  .brand-name{
    font-weight:500;font-size:21px;line-height:22px;color:var(--grey);letter-spacing:.5px;
  }
  .keywords{
    position:absolute;top:53px;list-style:none;
    font-size:13.5px;font-weight:500;color:var(--ink);line-height:16px;
  }
  .keywords li{display:flex;align-items:center;gap:5px}
  .keywords li::before{
    content:"";width:9px;height:9px;border:2px solid var(--blue);border-radius:50%;flex:none;
  }
  .keywords-main{left:226px}
  .keywords-extra{left:398px}
  .divider{
    position:absolute;left:375px;top:38px;width:2px;height:90px;
    background:linear-gradient(180deg,rgba(0,0,0,0),rgba(0,0,0,.09),rgba(0,0,0,0));
  }
  .photo{
    position:absolute;left:486px;top:0;width:124px;height:141px;
    background:radial-gradient(ellipse at 55% 55%,#dcdcdc 0%,#eeeeee 45%,rgba(245,245,245,0) 75%);
  }
  .headline{
    position:absolute;right:45px;top:16px;text-align:right;
    font-weight:800;font-size:20px;line-height:24.5px;color:var(--white);
  }
  .headline .accent{color:var(--headline-yellow)}
</style>
</head>
<body>
  <section class="banner" aria-label="TKV Corner channel art">
    <div class="photo" role="img" aria-label="Photo of a hand in a white shirt touching a network of people icons"></div>

    <svg class="shapes" viewBox="0 0 1000 141" aria-hidden="true">
      <polygon points="0,0 52,0 0,72" fill="var(--yellow)"/>
      <polygon points="0,64 0,141 45,141" fill="var(--blue)"/>
      <polygon points="692,13 715,13 631,141 612,141" fill="var(--yellow)"/>
      <polygon points="612,141 644,110 1000,118 1000,141" fill="var(--blue)"/>
      <defs>
        <linearGradient id="redFill" x1="0" y1="0" x2="0" y2="1">
          <stop offset="0" stop-color="var(--red-dark)"/>
          <stop offset="0.4" stop-color="var(--red)"/>
          <stop offset="1" stop-color="var(--red-dark)"/>
        </linearGradient>
      </defs>
      <polygon points="740,0 1000,0 1000,118 841,133 642,110" fill="url(#redFill)"/>
      <polyline points="642,112 841,135 1000,120" fill="none" stroke="var(--white)" stroke-width="3"/>
      <line x1="740" y1="0" x2="642" y2="110" stroke="var(--white)" stroke-width="3"/>
    </svg>

    <div class="brand">
      <span class="brand-mark"></span>
      <span class="brand-name">TKV<br>Corner</span>
    </div>

    <ul class="keywords keywords-main">
      <li>Human Resources</li>
      <li>Performance</li>
      <li>Better</li>
      <li>Faster</li>
    </ul>
    <div class="divider"></div>
    <ul class="keywords keywords-extra">
      <li>Easier</li>
      <li>Business</li>
      <li>Improve</li>
      <li>Health</li>
    </ul>

    <p class="headline">
      A better and faster<br>
      <span class="accent">human resources to</span><br>
      help business improve<br>
      <span class="accent">Your productivity</span>
    </p>
  </section>
</body>
</html>
```